Vornfield Business Cards

Logo files are included. Full "Vornfield" logo should be included on the back of the business card. The H symbol should be included on the front with the contact information.

Vornfield, LLC is the company name and we do commercial construction and real estate development consulting services. Look for a fairly simple card design utilizing our logo.

```html
<!DOCTYPE html>
<html lang="en">
<head>
<meta charset="utf-8">
<title>Vornfield Business Cards</title>
<link href="https://fonts.googleapis.com/css2?family=Montserrat:wght@400;500;600;700&display=swap" rel="stylesheet">
<style>
  :root {
    --navy: #1c3a4f;
    --gold: #e9ae0f;
    --paper: #ffffff;
    --ink-grey: #6d7276;
    --backdrop: #2a2b2d;
  }
  * { box-sizing: border-box; margin: 0; padding: 0; }
  html, body { width: 1200px; height: 1024px; overflow: hidden; }
  body {
    background: var(--backdrop);
    font-family: "Montserrat", Arial, sans-serif;
    position: relative;
  }
  .card {
    position: absolute;
    left: 300px;
    width: 600px;
    height: 343px;
    box-shadow: 0 14px 34px rgba(0,0,0,.55);
  }
  .card--front { top: 139px; background: var(--navy); }
  .card--back { top: 542px; background: var(--paper); }

  /* front */
  .front-brand {
    position: absolute;
    top: 96px; left: 0; right: 0;
    text-align: center;
    color: var(--paper);
    font-weight: 600;
    font-size: 56px;
    letter-spacing: 3px;
  }
  .front-rule {
    position: absolute;
    top: 222px; left: 0; right: 0;
    height: 1px;
    background: var(--gold);
  }
  .web-pill {
    position: absolute;
    top: 209px; left: 50%;
    transform: translateX(-50%);
    background: var(--gold);
    color: var(--navy);
    border-radius: 8px;
    padding: 5px 22px;
    font-size: 14px;
    font-weight: 500;
    letter-spacing: 4px;
  }

  /* back */
  .contact {
    position: absolute;
    top: 44px; left: 352px;
    color: var(--ink-grey);
    font-size: 13.5px;
    line-height: 1.25;
  }
  .contact__address { margin-bottom: 14px; }
  .contact__row { display: flex; align-items: center; gap: 8px; margin-bottom: 5px; }
  .contact__icon { width: 14px; height: 14px; flex: none; }
  .holder {
    position: absolute;
    left: 44px; top: 196px;
  }
  .holder__name {
    font-size: 27px;
    font-weight: 700;
    color: var(--navy);
    letter-spacing: .5px;
  }
  .holder__name span { color: var(--gold); }
  .holder__role {
    font-size: 15px;
    color: var(--ink-grey);
    margin-top: 2px;
  }
  .back-brand {
    position: absolute;
    right: 40px; bottom: 40px;
    color: var(--navy);
    font-weight: 600;
    font-size: 38px;
    letter-spacing: 2px;
  }
</style>
</head>
<body>
  <section class="card card--front">
    <div class="front-brand">VORNFIELD</div>
    <div class="front-rule"></div>
    <div class="web-pill">www.vornfieldllc.com</div>
  </section>

  <section class="card card--back">
    <div class="contact">
      <p class="contact__address">123, Your Street Name, your<br>city, lane 00125</p>
      <p class="contact__row">
        <svg class="contact__icon" viewBox="0 0 14 14"><circle cx="7" cy="7" r="7" fill="var(--gold)"/><path d="M4.5 3.8l1.2-.3.8 1.8-.8.6a5 5 0 0 0 2.4 2.4l.6-.8 1.8.8-.3 1.2c-3 .3-6-2.7-5.7-5.7z" fill="#fff"/></svg>
        (555) 214-0198
      </p>
      <p class="contact__row">
        <svg class="contact__icon" viewBox="0 0 14 14"><circle cx="7" cy="7" r="7" fill="var(--gold)"/><rect x="3.6" y="4.6" width="6.8" height="4.8" fill="none" stroke="#fff" stroke-width="1"/><path d="M3.6 4.6L7 7.4l3.4-2.8" fill="none" stroke="#fff" stroke-width="1"/></svg>
        info@vornfieldllc.com
      </p>
      <p class="contact__row">
        <svg class="contact__icon" viewBox="0 0 14 14"><circle cx="7" cy="7" r="7" fill="var(--gold)"/><circle cx="7" cy="7" r="3.6" fill="none" stroke="#fff" stroke-width=".9"/><path d="M3.4 7h7.2M7 3.4v7.2" stroke="#fff" stroke-width=".9"/></svg>
        www.vornfieldllc.com
      </p>
    </div>
    <div class="holder">
      <h1 class="holder__name">JONE <span>SMITH</span></h1>
      <p class="holder__role">CEO/Owner</p>
    </div>
    <div class="back-brand">VORNFIELD</div>
  </section>
</body>
</html>
```